Veranaxis Business Card and Letter Head

We are a leadership assessment consultancy based in Sydney, Australia. We help executive-level decison-makers select leaders for more senior level roles in corporate and government organisations. Our methodology is based on the latest research from the field of neuroscience.
We need a business card design and matching letter head that presents our company, Veranaxis, as a:
1. trusted adviser to senior executive-level decison makers
2. niche consultancy who are experts in the field of assessing leadership talent
3. results-focused solution provider who balance scientific methods with pragmatic solutions
The following company details should be used in all designs:
Company Name: Veranaxis
Details (for business card):
Daniel Prescott
Senior Talent Officer
Level 29, Brenning Tower
7 Brenning Square
Sydney, NSW 2000 Australia
Phone: 1300 482 716
Mobile: 0412 573 208
Email: daniel.prescott@veranaxis.com.au
Website: veranaxis.com.au
I have attached the logo for Veranaxis (for both a white and black background) - your business card and letter head designs must incoporate this logo and colour scheme.
Thanks for your interest in this project, I'm looking forward to receiving your ideas.
Regards,
Daniel
Executive-level decison-makers in corporate and government organisations (e.g., CEO, VP, Head of Human Resources)
Leadership

```html
<!DOCTYPE html>
<html lang="en">
<head>
<meta charset="utf-8">
<title>Veranaxis Business Card</title>
<link href="https://fonts.googleapis.com/css2?family=Questrial&display=swap" rel="stylesheet">
<style>
  :root {
    --stage: #dfe3e6;
    --card-dark: #4b4b4d;
    --card-light: #ffffff;
    --ink: #3a3a3c;
    --ink-soft: #5a5a5c;
    --accent: #b3262d;
    --mark-light: #e9e9ea;
    --tagline-dark: #8c8c8e;
  }
  * { box-sizing: border-box; margin: 0; padding: 0; }
  html, body {
    width: 1200px;
    height: 960px;
    overflow: hidden;
    background: var(--stage);
    font-family: "Questrial", "Century Gothic", sans-serif;
  }
  .stage {
    width: 1200px;
    height: 960px;
    display: flex;
    flex-direction: column;
    align-items: center;
    justify-content: center;
    gap: 40px;
  }
  .card {
    width: 620px;
    height: 380px;
    position: relative;
    box-shadow: 0 6px 18px rgba(0,0,0,0.18);
  }
  /* Front */
  .card--front { background: var(--card-dark); }
  .card--front .brand {
    position: absolute;
    left: 40px;
    bottom: 44px;
  }
  .brand-row {
    display: flex;
    align-items: center;
    gap: 14px;
  }
  .brand-square {
    width: 56px;
    height: 56px;
    background: var(--mark-light);
  }
  .card--front .brand-name {
    color: var(--mark-light);
    font-size: 48px;
    line-height: 1;
    letter-spacing: 0.5px;
  }
  .card--front .brand-tagline {
    margin-top: 6px;
    margin-left: 70px;
    color: var(--tagline-dark);
    font-size: 13px;
    letter-spacing: 1.2px;
    text-transform: uppercase;
  }
  /* Back */
  .card--back {
    background: var(--card-light);
    color: var(--ink);
  }
  .card--back .brand {
    position: absolute;
    left: 36px;
    top: 30px;
  }
  .card--back .brand-row { gap: 9px; }
  .card--back .brand-square {
    width: 26px;
    height: 26px;
    background: var(--ink);
  }
  .card--back .brand-name {
    color: var(--ink);
    font-size: 25px;
    line-height: 1;
  }
  .card--back .brand-tagline {
    margin-top: 3px;
    margin-left: 35px;
    color: var(--accent);
    font-size: 7.5px;
    letter-spacing: 0.9px;
    text-transform: uppercase;
  }
  .person {
    position: absolute;
    left: 40px;
    top: 124px;
  }
  .person-name {
    font-size: 22px;
    letter-spacing: 0.8px;
    line-height: 1.15;
  }
  .person-title {
    font-size: 15px;
    letter-spacing: 0.6px;
    color: var(--ink-soft);
  }
  .address {
    position: absolute;
    left: 318px;
    top: 146px;
    font-style: normal;
    font-size: 13.5px;
    line-height: 1.35;
    letter-spacing: 0.6px;
    color: var(--ink-soft);
  }
  .contact {
    position: absolute;
    left: 318px;
    top: 238px;
    list-style: none;
    font-size: 14px;
    line-height: 1.4;
    letter-spacing: 0.5px;
  }
  .contact-label {
    color: var(--accent);
    font-weight: 700;
  }
  .contact-divider {
    margin: 0 12px;
    color: var(--ink-soft);
  }
</style>
</head>
<body>
<main class="stage">
  <section class="card card--front" aria-label="Business card front">
    <div class="brand">
      <div class="brand-row">
        <span class="brand-square"></span>
        <span class="brand-name">Veranaxis</span>
      </div>
      <p class="brand-tagline">Assessing Executive Leaders</p>
    </div>
  </section>

  <section class="card card--back" aria-label="Business card back">
    <div class="brand">
      <div class="brand-row">
        <span class="brand-square"></span>
        <span class="brand-name">Veranaxis</span>
      </div>
      <p class="brand-tagline">Assessing Executive Leaders</p>
    </div>

    <div class="person">
      <p class="person-name">Daniel Prescott</p>
      <p class="person-title">Senior Talent Officer</p>
    </div>

    <address class="address">
      Level 29, Brenning Tower<br>
      7 Brenning Square<br>
      Sydney, NSW 2000 Australia
    </address>

    <ul class="contact">
      <li><span class="contact-label">P:</span> 1300 482 716<span class="contact-divider">|</span><span class="contact-label">M:</span> 0412 573 208</li>
      <li><span class="contact-label">E:</span> daniel.prescott@veranaxis.com.au</li>
      <li><span class="contact-label">W:</span> veranaxis.com.au</li>
    </ul>
  </section>
</main>
</body>
</html>
```